Our desktop web app builder needs a redesign

We want to redesign our low-code web app builder called Fernhold. Fernhold runs in desktop environments and is aimed at IT professionals and developers.

The UI consists of a button bar, multiple panels and a tabbed working area. We are looking to completely change the look and feel of the application interfaces, while keeping the layout and functionality the same.

We would like to see your ideas for fonts, sizing, colour, icons and any other visual UI element. Your work can be a rough mockup of your design ideas, and does not need to be pixel perfect. Legibility and optimised use of space are key.

More details about the app and how it works here: https://fernhold.software/

If we like your ideas, we will get in touch with you and work with you to develop the new design in greater detail.

```html
<!DOCTYPE html>
<html lang="en">
<head>
<meta charset="utf-8">
<title>Fernhold Designer Redesign</title>
<link href="https://fonts.googleapis.com/css2?family=Roboto:wght@400;500;700&display=swap" rel="stylesheet">
<style>
:root{
  --bg:#8a8a8a;
  --white:#ffffff;
  --ink:#1e1e1e;
  --muted:#9a9a9a;
  --accent:#00b3d6;
  --pane:#d6d6d6;
  --pane-dark:#c4c4c4;
  --toolbar:#4a4a4a;
  --tint:#e4f7fb;
}
*{box-sizing:border-box;margin:0;padding:0}
html,body{width:1200px;height:2449px;overflow:hidden;background:var(--bg)}
body{font-family:"Roboto",sans-serif;color:var(--ink)}
.stage{position:absolute;left:0;top:0;width:1262px;height:2576px;transform:scale(0.9509);transform-origin:0 0;background:var(--bg)}
.a{position:absolute}
/* designer */
.designer{left:25px;top:32px;width:1212px;height:658px;background:var(--white)}
.titlebar{left:0;top:0;width:1212px;height:44px;font-size:10px}
.menu span{margin-right:14px}
.toolbar{left:0;top:44px;width:1212px;height:42px;background:var(--toolbar);display:flex;align-items:center;gap:11px;padding-left:18px}
.toolbar svg{width:18px;height:18px}
.explorer{left:0;top:86px;width:215px;height:572px;background:var(--pane)}
.tabhead{height:28px;background:var(--pane-dark);font-size:9.5px;padding:10px 0 0 12px}
.tabhead .lbl{position:absolute;left:4px;top:3px;width:104px;height:25px;background:#e2e2e2;padding:9px 8px;white-space:nowrap;overflow:hidden}
.tree{font-size:9.5px}
.tree div{position:absolute;white-space:nowrap}
.sel{background:#b8b8b8}
.work{left:215px;top:86px;width:781px;height:572px;background:var(--white)}
.tab{left:4px;top:3px;width:78px;height:26px;background:var(--accent);color:#fff;font-size:10px;font-weight:500;text-align:center;line-height:26px;border-radius:2px}
.card{position:absolute;width:107px;height:34px;background:#fff;box-shadow:0 1px 4px rgba(0,0,0,.22);border-radius:3px;font-size:9.5px;font-weight:500;display:flex;align-items:center;padding-left:12px;gap:9px;white-space:nowrap;overflow:hidden}
.card.wide{width:150px}
.card svg{width:14px;height:14px;flex:none}
.box{position:absolute;background:#fff;box-shadow:0 1px 5px rgba(0,0,0,.2)}
.node{position:absolute;font-size:9.5px;font-weight:500;display:flex;align-items:center;gap:6px;white-space:nowrap}
.node svg{width:12px;height:12px}
.side{left:996px;top:86px;width:216px;height:572px;background:var(--pane)}
.bar{position:absolute;left:0;width:216px;height:15px;background:#b8b8b8;font-size:9px;padding:2px 12px}
.prop{position:absolute;left:14px;font-size:9px;white-space:nowrap}
.val{position:absolute;left:102px;width:114px;height:15px;background:#b8b8b8;font-size:9px;padding:2px 5px;white-space:nowrap}
.chk{position:absolute;left:102px;width:15px;height:13px;background:#b8b8b8}
/* editor */
.editor{left:45px;width:1171px;height:898px;background:var(--white)}
.logo{left:40px;top:30px;font-size:28px;font-weight:400;color:var(--accent);letter-spacing:.5px;display:flex;align-items:center;gap:10px}
.logo i{width:30px;height:30px;border-radius:50%;border:3px solid var(--accent);display:block}
.search{left:257px;top:30px;width:310px;height:37px;border-radius:19px;background:#fff;box-shadow:0 1px 6px rgba(0,0,0,.18);font-size:16px;padding:9px 20px}
.search svg{position:absolute;right:14px;top:11px;width:16px;height:16px}
.addcol{left:603px;top:30px;width:150px;height:37px;border-radius:19px;background:var(--accent);color:#fff;font-weight:700;font-size:16px;padding:9px 15px;white-space:nowrap}
.icons{left:790px;top:40px;display:flex;gap:14px}
.icons svg{width:16px;height:16px}
.avatar{left:902px;top:20px;width:50px;height:50px;border-radius:50%;background:linear-gradient(#8a8f96,#4b5058)}
.hello{left:960px;top:27px;font-size:15px;color:#b5b5b5}
.uname{left:960px;top:48px;font-size:16px;white-space:nowrap}
.hline{left:0;top:95px;width:1171px;height:1px;background:#e6e6e6}
.nav{font-size:16px;font-weight:700}
.navsel{left:40px;top:126px;width:166px;height:51px;background:var(--accent);color:#fff;padding:16px 25px;border-radius:2px}
.content{left:235px;top:97px;width:936px;height:801px;background:var(--tint);border-top-left-radius:14px}
.lab{position:absolute;left:63px;font-size:16px;white-space:nowrap}
.bold{font-weight:700}
.field{position:absolute;left:307px;width:400px;height:43px;background:#fff;font-size:16px;padding:12px 7px;white-space:nowrap}
.field svg{position:absolute;right:14px;top:17px;width:10px;height:8px}
.raised{box-shadow:0 1px 5px rgba(0,0,0,.18)}
.btn{position:absolute;left:307px;width:156px;height:42px;background:var(--accent);color:#fff;font-weight:700;font-size:16px;padding:12px 7px;border-radius:2px;white-space:nowrap}
.info{position:absolute;left:60px;width:580px;height:52px;background:#fff;font-size:15px;padding:17px 22px;white-space:nowrap;overflow:hidden}
.save{position:absolute;left:502px;width:95px;height:38px;background:var(--accent);color:#fff;font-weight:700;font-size:16px;text-align:center;line-height:38px}
.cancel{position:absolute;left:611px;width:95px;height:38px;background:#fff;font-weight:700;font-size:16px;text-align:center;line-height:38px}
.drop{position:absolute;left:307px;width:400px;height:187px;background:#fff;box-shadow:0 3px 8px rgba(0,0,0,.2);font-size:16px}
.drop div{position:absolute;white-space:nowrap}
</style>
</head>
<body>
<div class="stage">

<!-- Designer window -->
<section class="a designer">
  <div class="a titlebar">
    <div class="a" style="left:12px;top:14px;width:26px;height:14px;border:2px solid var(--accent);border-radius:50%"></div>
    <div class="a menu" style="left:56px;top:17px"><span>File</span><span>Edit</span><span>Inser</span><span>Run</span><span>Window</span><span>Help</span></div>
    <div class="a" style="left:487px;top:18px">Appwithtable_stable.sapz - Fernhold Designer Wind</div>
  </div>
  <div class="a toolbar">
    <svg viewBox="0 0 18 18"><path d="M2 5h5l2 2h7v8H2z" fill="none" stroke="#fff" stroke-width="1.5"/></svg>
    <svg viewBox="0 0 18 18"><rect x="3" y="3" width="12" height="12" fill="none" stroke="#fff" stroke-width="1.5"/><rect x="6" y="3" width="6" height="4" fill="#fff"/></svg>
    <svg viewBox="0 0 18 18"><path d="M4 2h7l3 3v11H4z" fill="none" stroke="#fff" stroke-width="1.5"/></svg>
    <svg viewBox="0 0 18 18"><path d="M2 4h5l2 2h7v9H2z" fill="#fff"/></svg>
    <svg viewBox="0 0 18 18"><path d="M3 5h12M3 9h12M3 13h12" stroke="#fff" stroke-width="2"/></svg>
    <svg viewBox="0 0 18 18"><path d="M3 4h2M7 4h8M3 9h2M7 9h8M3 14h2M7 14h8" stroke="#fff" stroke-width="2"/></svg>
    <svg viewBox="0 0 18 18"><path d="M2 4h5l2 2h7v9H2z" fill="none" stroke="#fff" stroke-width="1.5"/></svg>
    <svg viewBox="0 0 18 18"><path d="M6 2v14M12 2v14M3 5l3-3 3 3M9 13l3 3 3-3" fill="none" stroke="#fff" stroke-width="1.5"/></svg>
    <svg viewBox="0 0 18 18"><rect x="2" y="4" width="14" height="10" fill="none" stroke="#fff" stroke-width="1.5"/><path d="M4 8h10M4 11h10" stroke="#fff"/></svg>
    <svg viewBox="0 0 18 18"><path d="M4 2l11 7-11 7z" fill="#fff"/></svg>
    <svg viewBox="0 0 18 18"><path d="M9 4H3v10h6M7 9h9M13 6l3 3-3 3" fill="none" stroke="#fff" stroke-width="1.5"/></svg>
  </div>

  <aside class="a explorer">
    <div class="tabhead" style="position:relative"><div class="lbl">Application Explorer</div><div class="a" style="left:163px;top:8px;font-size:10px">⚲ &nbsp;⇱ &nbsp;✕</div></div>
    <div class="tree">
      <div style="left:14px;top:51px">▾ &nbsp;⛭ Bugbear</div>
      <div style="left:28px;top:71px">▾ &nbsp;▢ Pages</div>
      <div style="left:44px;top:90px">▸ &nbsp;■ Tracker</div>
      <div style="left:44px;top:109px">▸ &nbsp;▤ AddBug</div>
      <div style="left:44px;top:128px">▸ &nbsp;▤ Home</div>
      <div class="sel" style="left:0;top:145px;width:215px;height:16px"></div>
      <div style="left:44px;top:148px">▸ &nbsp;▤ ViewBug</div>
      <div style="left:40px;top:168px">≡ &nbsp;Types</div>
      <div style="left:44px;top:189px">▸ &nbsp;☷ Templates</div>
      <div style="left:40px;top:208px">✎ &nbsp;Styles</div>
      <div style="left:40px;top:228px">⚙ &nbsp;Settings</div>
      <div style="left:44px;top:246px">▸ &nbsp;■ EmbeddedFiles</div>
      <div style="left:44px;top:263px">▸ &nbsp;⇅ Connectors</div>
    </div>
  </aside>

  <main class="a work">
    <div class="a tab">ViewBug</div>
    <div class="card" style="left:4px;top:42px"><svg viewBox="0 0 14 14"><path d="M2 2h10M7 2v10M5 12h4M2 2v2M12 2v2" stroke="#333" fill="none"/></svg>Label1</div>
    <div class="box" style="left:8px;top:92px;width:516px;height:415px"></div>
    <div class="box" style="left:536px;top:92px;width:214px;height:415px"></div>

    <div class="node" style="left:20px;top:105px">▾ ⋮⋮⋮ LayoutTable1</div>
    <div class="node" style="left:36px;top:128px">▾ ▢ DetailsPanel</div>
    <div class="node" style="left:52px;top:151px">▾ ⋮⋮⋮ LayoutTable2</div>
    <div class="card" style="left:50px;top:174px">T&nbsp; Label3</div>
    <div class="card" style="left:167px;top:174px">T&nbsp; ReportedByL...</div>
    <div class="card" style="left:283px;top:174px">T&nbsp; Label2</div>
    <div class="card" style="left:50px;top:217px">⧉&nbsp; ReportedOn...</div>
    <div class="card" style="left:167px;top:217px">⧉&nbsp; ReportedByT...</div>
    <div class="card" style="left:283px;top:217px">⧉&nbsp; StatusDropD...</div>
    <div class="card" style="left:399px;top:217px">▣&nbsp; TrackerImage</div>
    <div class="node" style="left:36px;top:268px">▾ ⋮⋮⋮ LayoutGrid1</div>
    <div class="node" style="left:52px;top:297px">▾ ⋮⋮⋮ LayoutTable3</div>
    <div class="card" style="left:50px;top:320px">T&nbsp; TitleLabe</div>
    <div class="card" style="left:167px;top:320px">▣&nbsp; EditTitleImage</div>
    <div class="card" style="left:283px;top:320px">▣&nbsp; SaveTitleIma...</div>
    <div class="card" style="left:50px;top:369px">⧉&nbsp; TitleTextBox</div>
    <div class="node" style="left:52px;top:421px">▾ ⋮⋮⋮ LayoutTable4</div>
    <div class="card" style="left:50px;top:444px">T&nbsp; DescriptionL...</div>
    <div class="card" style="left:167px;top:444px">▣&nbsp; EditDescripti...</div>
    <div class="card" style="left:283px;top:444px">▣&nbsp; SaveDescript...</div>

    <div class="node" style="left:552px;top:107px">▢ &nbsp;Panel</div>
    <div class="card wide" style="left:550px;top:132px">T&nbsp; Label3</div>
    <div class="card wide" style="left:550px;top:175px">⋮⋮⋮&nbsp; CommentDataGrid</div>
    <div class="card wide" style="left:550px;top:218px">⧉&nbsp; CommentTextBox</div>
    <div class="card wide" style="left:550px;top:261px">☝&nbsp; PostCommentBut...</div>
    <div class="a" style="left:767px;top:10px;width:7px;height:184px;background:#bdbdbd"></div>
  </main>

  <aside class="a side">
    <div class="tabhead" style="position:relative"><div class="lbl">Toolbox</div><div class="a" style="left:164px;top:8px;font-size:10px">⚲ &nbsp;⇱ &nbsp;✕</div></div>
    <div class="bar" style="top:35px">View<span style="float:right">▾</span></div>
    <div class="bar" style="top:56px">Layout<span style="float:right">▾</span></div>
    <div class="a" style="left:0;top:244px;width:216px;height:28px;background:var(--pane-dark)"></div>
    <div class="a" style="left:4px;top:248px;width:104px;height:24px;background:#e2e2e2;font-size:9px;padding:7px 8px;white-space:nowrap;overflow:hidden">Properties (DataG...</div>
    <div class="a" style="left:164px;top:254px;font-size:10px">⚲ &nbsp;⇱ &nbsp;✕</div>
    <div class="prop" style="top:290px">Name</div><div class="val" style="top:288px">HistoryDataGrid</div>
    <div class="prop" style="top:311px">Data</div>
    <div class="prop" style="top:331px">Columns</div><div class="val" style="top:329px">(Collection)</div>
    <div class="prop" style="top:353px">Optional</div>
    <div class="prop" style="top:374px">Allow Export</div><div class="chk" style="top:373px"></div>
    <div class="prop" style="top:393px">Display Search Bar</div><div class="chk" style="top:392px"></div>
    <div class="prop" style="top:413px">Selectable Data</div><div class="chk" style="top:412px"></div>
    <div class="prop" style="top:433px">Selectable Data</div><div class="val" style="top:431px">true</div>
  </aside>
</section>

<!-- Column editor -->
<section class="a editor" style="top:720px">
  <div class="a logo"><i></i>FERNHOLD</div>
  <div class="a search">Search<svg viewBox="0 0 16 16"><circle cx="7" cy="7" r="5" fill="none" stroke="#111" stroke-width="2"/><path d="M11 11l4 4" stroke="#111" stroke-width="2"/></svg></div>
  <div class="a addcol">ADD COLUMN ⌄</div>
  <div class="a icons">
    <svg viewBox="0 0 16 16"><ellipse cx="8" cy="7" rx="7" ry="5.5" fill="#111"/><path d="M4 11l-1 4 4-3z" fill="#111"/></svg>
    <svg viewBox="0 0 16 16"><path d="M8 1c3 0 4 3 4 5v4l2 2H2l2-2V6c0-2 1-5 4-5zM6 13h4a2 2 0 01-4 0z" fill="#111"/></svg>
    <svg viewBox="0 0 16 16"><path d="M3 4h10M6 4V2h4v2M4 4l1 11h6l1-11M7 7v6M9 7v6" fill="none" stroke="#111" stroke-width="1.3"/></svg>
  </div>
  <div class="a avatar" role="img" aria-label="User profile photo"></div>
  <div class="a hello">Hello</div>
  <div class="a uname">Marlow Penn <span style="margin-left:8px">⌄</span></div>
  <div class="a hline"></div>
  <div class="a nav navsel">FirstName</div>
  <div class="a nav" style="left:65px;top:208px">LastName</div>
  <div class="a nav" style="left:65px;top:273px">Age</div>
  <div class="a nav" style="left:65px;top:336px">Height</div>
  <div class="a content">
    <div class="lab" style="top:62px">Name</div><div class="lab" style="left:314px;top:62px">FirstName</div>
    <div class="lab" style="top:130px">Column Type</div>
    <div class="field" style="top:118px">Data-Bound<svg viewBox="0 0 10 8"><path d="M1 2l4 4 4-4" fill="none" stroke="#111" stroke-width="1.5"/></svg></div>
    <div class="lab" style="top:184px">Text</div>
    <div class="field" style="top:172px">Data-Bound<svg viewBox="0 0 10 8"><path d="M1 2l4 4 4-4" fill="none" stroke="#111" stroke-width="1.5"/></svg></div>
    <div class="lab bold" style="top:239px">Events</div>
    <div class="lab" style="top:289px">Click</div>
    <div class="btn" style="top:278px">CreateEventHandler</div>
    <div class="lab" style="top:366px">Header Text</div>
    <div class="field" style="top:355px">First Name<svg viewBox="0 0 10 8"><path d="M1 2l4 4 4-4" fill="none" stroke="#111" stroke-width="1.5"/></svg></div>
    <div class="lab" style="top:420px">Alignment</div>
    <div class="field" style="top:409px">Left<svg viewBox="0 0 10 8"><path d="M1 2l4 4 4-4" fill="none" stroke="#111" stroke-width="1.5"/></svg></div>
    <div class="lab" style="top:475px">Cell Display</div>
    <div class="field" style="top:463px">Default<svg viewBox="0 0 10 8"><path d="M1 2l4 4 4-4" fill="none" stroke="#111" stroke-width="1.5"/></svg></div>
    <div class="lab" style="top:530px">Visible</div>
    <svg class="a" style="left:315px;top:532px;width:14px;height:14px" viewBox="0 0 14 14"><circle cx="7" cy="7" r="7" fill="var(--accent)"/><path d="M4 7l2 2 4-4" fill="none" stroke="#fff" stroke-width="1.6"/></svg>
    <div class="lab bold" style="top:605px">⌄ &nbsp;Column Type</div>
    <div class="info" style="top:641px">Choose whether the cell displays a value from a connector or the specified text</div>
    <div class="save" style="top:726px">SAVE</div>
    <div class="cancel" style="top:726px">CANCEL</div>
  </div>
</section>

<!-- Column editor with open header picker -->
<section class="a editor" style="top:1645px">
  <div class="a logo"><i></i>FERNHOLD</div>
  <div class="a search">Search<svg viewBox="0 0 16 16"><circle cx="7" cy="7" r="5" fill="none" stroke="#111" stroke-width="2"/><path d="M11 11l4 4" stroke="#111" stroke-width="2"/></svg></div>
  <div class="a addcol">ADD COLUMN ⌄</div>
  <div class="a icons">
    <svg viewBox="0 0 16 16"><ellipse cx="8" cy="7" rx="7" ry="5.5" fill="#111"/><path d="M4 11l-1 4 4-3z" fill="#111"/></svg>
    <svg viewBox="0 0 16 16"><path d="M8 1c3 0 4 3 4 5v4l2 2H2l2-2V6c0-2 1-5 4-5zM6 13h4a2 2 0 01-4 0z" fill="#111"/></svg>
    <svg viewBox="0 0 16 16"><path d="M3 4h10M6 4V2h4v2M4 4l1 11h6l1-11M7 7v6M9 7v6" fill="none" stroke="#111" stroke-width="1.3"/></svg>
  </div>
  <div class="a avatar" role="img" aria-label="User profile photo"></div>
  <div class="a hello">Hello</div>
  <div class="a uname">Marlow Penn <span style="margin-left:8px">⌄</span></div>
  <div class="a hline"></div>
  <div class="a nav navsel">FirstName</div>
  <div class="a nav" style="left:65px;top:208px">LastName</div>
  <div class="a nav" style="left:65px;top:273px">Age</div>
  <div class="a nav" style="left:65px;top:336px">Height</div>
  <div class="a content">
    <div class="lab" style="top:62px">Name</div><div class="lab" style="left:314px;top:62px">FirstName</div>
    <div class="lab" style="top:130px">Column Type</div>
    <div class="field raised" style="top:118px">Data-Bound<svg viewBox="0 0 10 8"><path d="M1 2l4 4 4-4" fill="none" stroke="#111" stroke-width="1.5"/></svg></div>
    <div class="lab" style="top:184px">Text</div>
    <div class="field raised" style="top:172px">Data-Bound<svg viewBox="0 0 10 8"><path d="M1 2l4 4 4-4" fill="none" stroke="#111" stroke-width="1.5"/></svg></div>
    <div class="lab bold" style="top:239px">Events</div>
    <div class="lab" style="top:289px">Click</div>
    <div class="btn" style="top:278px">CreateEventHandler</div>
    <div class="lab" style="top:366px">Header Text</div>
    <div class="field raised" style="top:355px">First Name<svg viewBox="0 0 10 8"><path d="M1 2l4 4 4-4" fill="none" stroke="#111" stroke-width="1.5"/></svg></div>
    <div class="lab" style="top:420px">Alignment</div>
    <div class="lab" style="top:475px">Cell Display</div>
    <div class="lab" style="top:530px">Visible</div>
    <div class="drop" style="top:396px">
      <div style="left:22px;top:9px">Expression</div>
      <div style="left:25px;top:35px"><span style="font-size:10px">▼</span>&nbsp; Session</div>
      <div style="left:44px;top:59px"><span style="font-size:10px">▼</span>&nbsp; LoggedInUser</div>
      <div style="left:80px;top:90px">ID</div>
      <div style="left:80px;top:114px">Name</div>
      <div style="left:80px;top:137px">Email</div>
      <div style="left:80px;top:161px">Roles</div>
    </div>
    <div class="lab bold" style="top:605px">⌄ &nbsp;Column Type</div>
    <div class="info" style="top:641px">Choose whether the cell displays a value from a connector or the specified text</div>
    <div class="save" style="top:726px">SAVE</div>
    <div class="cancel" style="top:726px">CANCEL</div>
  </div>
</section>

</div>
</body>
</html>
```